Grey Heron Estates Inc Business Card design

Grey Heron Estates Inc is a West Vancouver based boutique brokerage specializing in the marketing and sale of luxury and waterfront real estate.

This card is for Marlon Tevaki, Vice-President.

The card should have something modern and unique about. Some sort of gimmick would be nice.

I would like it to use or update the grey heron estates logo visible at www.greyheronestates-example.com

Very open to any design.

Target Market(s)

humans, the type with money

Industry/Entity Type

Marketing

Requirements
Must have
• The name Marlon Tevaki

Company name Grey Heron Estates Inc

Phone 604-512-3047

Fax 604-488-1630

email marlontevaki@mailbox-example.com

website www.marlontevaki-example.com

LOGO

tag line"A calm course to fine homes by the northern shore"

the attched pic of me if possible
Nice to have
• Something that would make people say "nice card" and not throw it in the garbage immediately, open to ideas
Should not have
• anything that looks like a template

```html
<!DOCTYPE html>
<html lang="en">
<head>
<meta charset="utf-8">
<title>Grey Heron Estates Inc — Marlon Tevaki</title>
<link rel="stylesheet" href="https://fonts.googleapis.com/css2?family=Cinzel:wght@400&family=Crimson+Text:wght@400&display=swap">
<style>
  :root {
    --card-black: #000000;
    --frame-white: #f2f2f2;
    --brand-grey: #8a8a8a;
    --tagline-grey: #6f6f6f;
    --text-white: #ffffff;
  }
  html, body {
    margin: 0;
    padding: 0;
    width: 1200px;
    height: 741px;
    overflow: hidden;
    background: var(--card-black);
  }
  .card {
    position: relative;
    width: 1200px;
    height: 741px;
    background: var(--card-black);
    overflow: hidden;
  }
  .card-frame {
    position: absolute;
    inset: 0;
  }
  .brand-name {
    position: absolute;
    left: 0;
    width: 1200px;
    top: 240px;
    margin: 0;
    text-align: center;
    font-family: "Cinzel", "Trajan Pro", serif;
    font-weight: 400;
    font-size: 50px;
    letter-spacing: 2px;
    line-height: 1;
    color: var(--brand-grey);
  }
  .tagline {
    position: absolute;
    left: 0;
    width: 1200px;
    top: 300px;
    margin: 0;
    text-align: center;
    font-family: "Cinzel", serif;
    font-weight: 400;
    font-size: 26px;
    letter-spacing: 2.8px;
    line-height: 1;
    color: var(--tagline-grey);
    text-transform: uppercase;
    white-space: nowrap;
  }
  .agent-name {
    position: absolute;
    left: 0;
    width: 1200px;
    top: 400px;
    margin: 0;
    text-align: center;
    font-family: "Crimson Text", "Palatino Linotype", serif;
    font-weight: 400;
    font-size: 90px;
    line-height: 1;
    color: var(--text-white);
  }
  .contact {
    position: absolute;
    left: 0;
    width: 1200px;
    top: 570px;
    margin: 0;
    padding: 0;
    list-style: none;
    text-align: center;
    font-family: "Crimson Text", "Palatino Linotype", serif;
    font-size: 32px;
    line-height: 41px;
    color: var(--text-white);
  }
</style>
</head>
<body>
  <main class="card">
    <svg class="card-frame" width="1200" height="741" viewBox="0 0 1200 741" aria-hidden="true">
      <rect x="15" y="15" width="1170" height="711" rx="13" ry="13" fill="none" stroke="var(--frame-white)" stroke-width="2"/>
    </svg>

    <h1 class="brand-name">Grey Heron Estates Inc.</h1>
    <p class="tagline">A calm course to fine homes by the northern shore</p>

    <h2 class="agent-name">Marlon Tevaki</h2>

    <ul class="contact">
      <li class="contact-phone">Phone 604-512-3047</li>
      <li class="contact-fax">Fax 604-488-1630</li>
      <li class="contact-email">marlontevaki@mailbox-example.com</li>
    </ul>
  </main>
</body>
</html>
```